Employee Benefits and Insurance Consulting

We are an existing company with over 30 years experience but are changing our name. We would like a simple design with grey tones.

Industry/Entity Type

Insurance

Contact Information for Business Card

Marlow Benefits Consulting
Gerald P Odell CEO
5172 Brackenfield Road
Harrowgate, TN 37842
gerald@marlowbx.com
865-412-3396 - O
865-247-5081 - C

```html
<!DOCTYPE html>
<html lang="en">
<head>
<meta charset="utf-8">
<title>Marlow Benefits Consulting – Business Card</title>
<link rel="stylesheet" href="https://fonts.googleapis.com/css2?family=Jost:wght@400&display=swap">
<style>
  :root {
    --backdrop-light: #b9b9b9;
    --backdrop-dark: #7a7a7a;
    --card-black: #0d0d0d;
    --card-silver-light: #f4f4f4;
    --card-silver-dark: #cfcfcf;
    --ink-grey: #6a6a6a;
    --ink-silver: #a8a8a8;
  }
  * { margin: 0; padding: 0; box-sizing: border-box; }
  html, body { width: 1200px; height: 1048px; overflow: hidden; }
  body {
    background: radial-gradient(ellipse at 50% 35%, var(--backdrop-light), var(--backdrop-dark));
    font-family: "Jost", "Futura", sans-serif;
    font-weight: 400;
    position: relative;
  }
  .card {
    position: absolute;
    width: 620px;
    height: 354px;
    border-radius: 3px;
    box-shadow: 0 10px 24px rgba(0,0,0,0.35);
  }
  .card--front {
    left: 500px; top: 90px;
    background: var(--card-black);
    display: flex; align-items: center; justify-content: center;
  }
  .card--back {
    left: 90px; top: 500px;
    background: linear-gradient(135deg, var(--card-silver-light), var(--card-silver-dark));
    display: flex; align-items: center; justify-content: space-between;
    padding: 0 44px 0 56px;
  }
  .brand {
    display: flex; align-items: center; gap: 14px;
    text-transform: uppercase;
  }
  .brand__name { display: flex; flex-direction: column; line-height: 1.15; }
  .brand__primary { font-size: 40px; letter-spacing: 0.32em; }
  .brand__secondary { font-size: 19px; letter-spacing: 0.06em; }
  .brand__mark { width: 18px; height: 18px; flex: none; }
  .card--front .brand { color: var(--ink-silver); }
  .card--front .brand__mark { background: var(--ink-silver); }
  .card--back .brand { color: var(--ink-grey); }
  .card--back .brand__primary { font-size: 32px; }
  .card--back .brand__secondary { font-size: 15px; }
  .card--back .brand__mark { background: var(--ink-grey); width: 14px; height: 14px; }
  .contact { color: var(--ink-grey); text-transform: uppercase; }
  .contact__name { font-size: 21px; letter-spacing: 0.05em; line-height: 1.1; }
  .contact__role { font-size: 19px; letter-spacing: 0.3em; margin-bottom: 8px; }
  .contact__list { list-style: none; font-size: 17px; letter-spacing: 0.03em; line-height: 1.45; }
  .contact__item { display: flex; align-items: flex-start; gap: 12px; white-space: nowrap; }
  .contact__icon { width: 16px; height: 16px; margin-top: 4px; flex: none; fill: var(--ink-grey); }
  .contact__spacer { width: 16px; flex: none; }
</style>
</head>
<body>
  <div class="card card--front">
    <div class="brand">
      <span class="brand__mark"></span>
      <span class="brand__name"><span class="brand__primary">Marlow</span><span class="brand__secondary">Benefits Consulting</span></span>
    </div>
  </div>

  <div class="card card--back">
    <div class="brand">
      <span class="brand__mark"></span>
      <span class="brand__name"><span class="brand__primary">Marlow</span><span class="brand__secondary">Benefits Consulting</span></span>
    </div>
    <div class="contact">
      <p class="contact__name">Gerald P Odell</p>
      <p class="contact__role">CEO</p>
      <ul class="contact__list">
        <li class="contact__item">
          <svg class="contact__icon" viewBox="0 0 16 16" aria-hidden="true"><path d="M8 0a5.5 5.5 0 0 0-5.5 5.5C2.5 10 8 16 8 16s5.5-6 5.5-10.5A5.5 5.5 0 0 0 8 0zm0 8a2.5 2.5 0 1 1 0-5 2.5 2.5 0 0 1 0 5z"/></svg>
          <span>5172 Brackenfield Road</span>
        </li>
        <li class="contact__item"><span class="contact__spacer"></span><span>Harrowgate, TN 37842</span></li>
        <li class="contact__item">
          <svg class="contact__icon" viewBox="0 0 16 16" aria-hidden="true"><path d="M0 3h16v10H0zM1.5 4.5v.4L8 9.3l6.5-4.4v-.4zM1.5 6.7v4.8h13V6.7L8 11z"/></svg>
          <span>gerald@marlowbx.com</span>
        </li>
        <li class="contact__item">
          <svg class="contact__icon" viewBox="0 0 16 16" aria-hidden="true"><path d="M1 4c0-2 3-3 7-3s7 1 7 3v1.5h-3.5V4h-7v1.5H1zM3.5 7h9l2 7h-13zM8 8.5a2 2 0 1 0 0 4 2 2 0 0 0 0-4z"/></svg>
          <span>865-412-3396</span>
        </li>
        <li class="contact__item">
          <svg class="contact__icon" viewBox="0 0 16 16" aria-hidden="true"><path d="M4 0h8a1 1 0 0 1 1 1v14a1 1 0 0 1-1 1H4a1 1 0 0 1-1-1V1a1 1 0 0 1 1-1zm.5 2v10.5h7V2zM8 13.3a.9.9 0 1 0 0 1.8.9.9 0 0 0 0-1.8z"/></svg>
          <span>865-247-5081</span>
        </li>
      </ul>
    </div>
  </div>
</body>
</html>
```